Business card design for strategy and management consulting company. Would like to have a clean and professional business card, based on the attached logo. The company is a strategy and management consulting company focusing on sustainable business modlels based on economic, social and environmental market opportunities. Preferably the logo should be included on both sides of the design.

Industry/Entity Type

Business

Contact Information for Business Card

Håvard Lilleby, CEO/Management consultant
havard.lilleby@quarvenpartners.example
Mob: +47 948 26 317
Office: Vikfjell gate 14, pb 312 sentrum, N-0172 Oslo Norway

Requirements
Must have
• Include attached logo
Nice to have
• Would like to have the logo on both sides
Should not have
• Many colours.

```html
<!DOCTYPE html>
<html lang="en">
<head>
<meta charset="utf-8">
<title>Quarven business card</title>
<link href="https://fonts.googleapis.com/css2?family=Open+Sans:wght@400;600;700&display=swap" rel="stylesheet">
<style>
  :root {
    --ink: #1c1c1c;
    --muted: #6b6b6b;
    --rule: #555555;
    --accent: #f2dc1f;
    --slate: #4a4a4c;
    --paper: #ffffff;
    --stage: #2a2a2c;
    --sky-top: #7ea6d6;
    --sky-mid: #c9dbeb;
    --sky-low: #9fb3c9;
  }
  * { box-sizing: border-box; margin: 0; padding: 0; }
  html, body { width: 1200px; height: 900px; overflow: hidden; }
  body {
    background: var(--stage);
    font-family: "Open Sans", Arial, sans-serif;
    position: relative;
  }
  .card {
    position: absolute;
    width: 600px;
    height: 343px;
    overflow: hidden;
    box-shadow: 0 10px 30px rgba(0,0,0,.45);
  }
  .card--front { left: 80px; top: 70px; }
  .card--back { left: 520px; top: 480px; background: var(--paper); }

  .sky-photo {
    position: absolute; inset: 0;
    background: linear-gradient(180deg, var(--sky-top) 0%, var(--sky-mid) 45%, #dfe8f0 60%, var(--sky-low) 100%);
  }
  .logo-band {
    position: absolute; left: 0; right: 0; top: 95px; height: 120px;
    background: rgba(255,255,255,.62);
    display: flex; align-items: center; justify-content: center;
  }
  .wordmark {
    display: flex; align-items: center; gap: 10px;
    font-weight: 700; color: var(--ink); letter-spacing: -1px;
  }
  .wordmark__dot {
    width: 14px; height: 14px; border-radius: 50%; background: var(--accent);
  }
  .logo-band .wordmark { font-size: 72px; }

  .back-art { position: absolute; inset: 0; }
  .back-logo { position: absolute; left: 36px; top: 122px; }
  .back-logo .wordmark { font-size: 46px; }
  .divider {
    position: absolute; left: 282px; top: 44px; width: 2px; height: 180px;
    background: var(--rule);
  }
  .contact { position: absolute; left: 300px; top: 44px; }
  .contact__name { font-size: 26px; font-weight: 600; color: var(--ink); line-height: 1.1; }
  .contact__title { font-size: 11.5px; color: var(--muted); margin-top: 2px; }
  .contact__list { list-style: none; margin-top: 22px; }
  .contact__item {
    display: flex; align-items: flex-start; gap: 7px;
    font-size: 11.5px; color: var(--ink); line-height: 1.35; margin-bottom: 4px;
  }
  .contact__icon {
    flex: none; width: 15px; height: 15px; margin-top: 1px;
    background: var(--accent); border-radius: 2px;
  }
</style>
</head>
<body>

  <section class="card card--front">
    <div class="sky-photo" role="img" aria-label="Photograph of a hot air balloon floating in a pale blue sky above distant hills"></div>
    <div class="logo-band">
      <div class="wordmark"><span>Quarven</span><span class="wordmark__dot"></span></div>
    </div>
  </section>

  <section class="card card--back">
    <svg class="back-art" viewBox="0 0 600 343" width="600" height="343" aria-hidden="true">
      <path d="M0 343 L0 338 C 200 314 430 244 600 220 L600 343 Z" fill="var(--slate)"/>
      <path d="M0 316 C 200 292 430 228 600 202 L600 209 C 430 236 210 306 0 332 Z" fill="var(--accent)"/>
    </svg>

    <div class="back-logo">
      <div class="wordmark"><span>Quarven</span><span class="wordmark__dot"></span></div>
    </div>

    <div class="divider"></div>

    <div class="contact">
      <h1 class="contact__name">Håvard Lilleby</h1>
      <p class="contact__title">CEO/Management consultant</p>
      <ul class="contact__list">
        <li class="contact__item">
          <svg class="contact__icon" viewBox="0 0 16 16"><rect x="5" y="3" width="6" height="10" rx="1" fill="none" stroke="#1c1c1c" stroke-width="1.3"/></svg>
          <span>+47 948 26 317</span>
        </li>
        <li class="contact__item">
          <svg class="contact__icon" viewBox="0 0 16 16"><rect x="3" y="4.5" width="10" height="7" fill="none" stroke="#1c1c1c" stroke-width="1.2"/><path d="M3 4.5 L8 8.5 L13 4.5" fill="none" stroke="#1c1c1c" stroke-width="1.2"/></svg>
          <span>havard.lilleby@quarvenpartners.example</span>
        </li>
        <li class="contact__item">
          <svg class="contact__icon" viewBox="0 0 16 16"><path d="M8 13.5 C5 9.5 4.5 8 4.5 6.5 A3.5 3.5 0 0 1 11.5 6.5 C11.5 8 11 9.5 8 13.5 Z" fill="#1c1c1c"/><circle cx="8" cy="6.5" r="1.3" fill="#f2dc1f"/></svg>
          <span>Vikfjell gate 14,<br>pb 312 sentrum, Oslo Norway</span>
        </li>
      </ul>
    </div>
  </section>

</body>
</html>
```